Business card for a shipping supplies business

Needing a business card design. Please see the logo. The logo with the white font should be used if there is a dark background.

We are looking for the following info on the card. Please see the sample info. We will need the info to be changed with a few different employee names and info but all will use the same template.

Business Name: The Crate Heron
Employee Name : Marcus Delaney
Position: Account Manager
Address: 4827 W. Ridge 418 S.
Fort Worth, TX 73948
email: Marcus@thecrateheron.example
telephone: 855-619-2740 x 207
website: www.getparcelkits.example

Target Market(s)

Businesses who ship products for online sales

Industry/Entity Type

Cardboard

Contact Information for Business Card

Name, title, address, website, logo, telephone number

Font styles to use
Sans Serif

Colors
EE7325
F08F49
F5BC92
FAE3D3
FDF4ED

Requirements
Must have
• Logo on back of card. Clean look, just logo, website address

```html
<!DOCTYPE html>
<html lang="en">
<head>
<meta charset="utf-8">
<title>The Crate Heron – Business Card</title>
<link rel="stylesheet" href="https://fonts.googleapis.com/css2?family=Montserrat:wght@400;700&display=swap">
<style>
  :root {
    --backdrop: #4d4b4a;
    --card-dark: #333333;
    --card-dark-soft: #3d3d3d;
    --orange-deep: #ad4a1b;
    --orange: #c4591f;
    --orange-light: #d46a35;
    --ink-light: #eeeeee;
    --ink-muted: #d8d8d8;
  }
  * { margin: 0; padding: 0; box-sizing: border-box; }
  html, body {
    width: 1200px; height: 1200px; overflow: hidden;
    background: var(--backdrop);
    font-family: "Montserrat", sans-serif;
  }
  .card {
    position: absolute; left: 244px;
    width: 700px; height: 400px;
    border-radius: 22px; overflow: hidden;
    background: linear-gradient(135deg, var(--card-dark-soft), var(--card-dark));
  }
  .card--front { top: 170px; }
  .card--back { top: 630px; }
  .card svg.art { position: absolute; inset: 0; }
  .brand-name {
    position: absolute; left: 48px; width: 400px; top: 190px;
    text-align: center; color: var(--ink-light);
    font-weight: 700; font-size: 38px; letter-spacing: 0.5px;
  }
  .website {
    position: absolute; left: 90px; top: 355px;
    display: flex; align-items: center; gap: 12px;
    color: var(--orange); font-size: 19px; letter-spacing: 1px;
  }
  .website span { border-bottom: 1.5px solid var(--orange); padding-bottom: 2px; }
  .contact {
    position: absolute; left: 380px; width: 300px; top: 37px;
    text-align: center; color: var(--ink-muted);
  }
  .contact__name { font-weight: 700; font-size: 28px; line-height: 34px; letter-spacing: 1.5px; color: var(--ink-light); }
  .contact__title { font-size: 18px; line-height: 24px; letter-spacing: 1.2px; margin-top: 7px; }
  .contact__icons { display: flex; justify-content: center; gap: 14px; margin-top: 106px; height: 27px; }
  .contact__details { margin-top: 21px; font-size: 18px; letter-spacing: 0.8px; line-height: 26px; }
  .contact__details p + p { margin-top: 10px; }
  .contact__email { font-size: 16px; }
</style>
</head>
<body>

<section class="card card--front">
  <svg class="art" width="700" height="400" viewBox="0 0 700 400">
    <defs>
      <linearGradient id="orangeFront" x1="0" y1="0" x2="0" y2="1">
        <stop offset="0" stop-color="var(--orange-deep)"/>
        <stop offset="1" stop-color="var(--orange)"/>
      </linearGradient>
    </defs>
    <path d="M458,0 Q530,120 614,200 Q530,280 458,400 L700,400 L700,0 Z" fill="url(#orangeFront)"/>
    <rect class="plane-art" x="629" y="160" width="64" height="80" rx="10" fill="var(--card-dark)" role="img" aria-label="Small airplane silhouette flying right"/>
  </svg>
  <div class="brand-name">The Crate Heron</div>
  <div class="website">
    <svg width="28" height="28" viewBox="0 0 28 28" fill="none" stroke="var(--orange)" stroke-width="2">
      <circle cx="14" cy="14" r="12"/>
      <ellipse cx="14" cy="14" rx="5" ry="12"/>
      <line x1="2" y1="14" x2="26" y2="14"/>
    </svg>
    <span>www.getparcelkits.example</span>
  </div>
</section>

<section class="card card--back">
  <svg class="art" width="700" height="400" viewBox="0 0 700 400">
    <defs>
      <linearGradient id="orangeBack" x1="0" y1="0" x2="0" y2="1">
        <stop offset="0" stop-color="var(--orange-light)"/>
        <stop offset="1" stop-color="var(--orange)"/>
      </linearGradient>
    </defs>
    <path d="M384,0 C320,70 306,140 306,200 C306,260 320,330 384,400 L34,400 Q110,270 190,200 Q110,130 34,0 Z" fill="url(#orangeBack)"/>
    <rect class="plane-art" x="207" y="160" width="64" height="80" rx="10" fill="var(--card-dark)" role="img" aria-label="Small airplane silhouette flying right"/>
  </svg>
  <div class="contact">
    <h1 class="contact__name">Marcus Delaney</h1>
    <p class="contact__title">Account Manager</p>
    <div class="contact__icons">
      <svg width="27" height="27" viewBox="0 0 28 28"><circle cx="14" cy="14" r="14" fill="var(--ink-muted)"/><path d="M14,6 a5.5,5.5 0 0 1 5.5,5.5 c0,4 -5.5,10 -5.5,10 s-5.5,-6 -5.5,-10 A5.5,5.5 0 0 1 14,6 Z" fill="var(--card-dark)"/><circle cx="14" cy="11.5" r="2.2" fill="var(--ink-muted)"/></svg>
      <svg width="27" height="27" viewBox="0 0 28 28"><circle cx="14" cy="14" r="14" fill="var(--ink-muted)"/><rect x="7" y="9" width="14" height="10" rx="1.5" fill="none" stroke="var(--card-dark)" stroke-width="1.8"/><path d="M7.5,10 L14,15 L20.5,10" fill="none" stroke="var(--card-dark)" stroke-width="1.8"/></svg>
      <svg width="27" height="27" viewBox="0 0 28 28"><circle cx="14" cy="14" r="14" fill="var(--ink-muted)"/><path d="M9,7 l3,0 l1.5,4 l-2,1.5 q1.5,3 4,4.5 l1.5,-2 l4,1.5 l0,3 q-1,1.5 -3,1.5 q-6,-1 -10,-7 q-1.5,-3 -1,-5 z" fill="var(--card-dark)"/></svg>
    </div>
    <div class="contact__details">
      <p>4827 W. Ridge 418 S.<br>Fort Worth, TX 73948</p>
      <p class="contact__email">Marcus@thecrateheron.example</p>
      <p>855-619-2740 x 207</p>
    </div>
  </div>
</section>

</body>
</html>
```